Lumen Wire Outlet - bag design for fiber optic cables

We need a packaging design for a clear ziplock bag that is 7" wide and 10" high. The design will be for a new line of fiber optic cable products. You can see the products on lumenwireoutlet.example. We would like to see designs that represent a superior quality product and an American brand. We want the equivalent of a nice retail bag that you would find in a store like Tech Haven. It should be a maximum of three colors. We really want something sharp, professional and eye catching, not whimsical or cartoonish. I've included a couple of examples below. I don't really like the designs attached but it will give you an idea. Please keep in mind the bag will be clear, not white.

Target Market(s)

Men 25-65

Industry/Entity Type

Optic

Colors

Designer to choose colors to be used in the design.

Requirements
Must have
• A clean design, not overly cluttered. These cables will be selling internationally so we need to show off the fact that we're an American brand. With that said, I don't want red, white and blue and over- the- top American. I would like something more subtle, classy that still says we are a USA brand. The bag should also incorporate the logo, which is attached. Please make it 3 colors maximum.
Nice to have
• clean, professional. The design doesn't need to have the colors in the logo. I'm open to any new colors introduced.
Should not have
• whimsical, colorful

```html
<!DOCTYPE html>
<html lang="en">
<head>
<meta charset="utf-8">
<title>Lumen Wire Outlet – OFC Bag</title>
<link href="https://fonts.googleapis.com/css2?family=Roboto+Condensed:wght@400;700&display=swap" rel="stylesheet">
<style>
  :root {
    --backdrop: #dcdddc;
    --bag: #8c2453;
    --bag-light: #a2466f;
    --bag-deep: #7a1c46;
    --ink: #ffffff;
    --cable: #4a4d55;
  }
  html, body {
    margin: 0;
    width: 1200px;
    height: 1200px;
    overflow: hidden;
    background: var(--backdrop);
    font-family: "Roboto Condensed", "Arial Narrow", sans-serif;
  }
  .bag {
    position: absolute;
    left: 250px;
    top: 100px;
    width: 700px;
    height: 1000px;
    background: linear-gradient(160deg, var(--bag) 0%, var(--bag-light) 45%, var(--bag) 75%, var(--bag-deep) 100%);
    color: var(--ink);
    overflow: hidden;
  }
  .seal-line {
    position: absolute;
    left: 30px;
    right: 30px;
    top: 110px;
    height: 2px;
    background: rgba(255,255,255,0.25);
  }
  .product-view {
    position: absolute;
    left: 70px;
    top: 170px;
    width: 460px;
    height: 780px;
    border-radius: 50% / 48%;
    background: radial-gradient(ellipse at 50% 45%, rgba(255,255,255,0.12) 0%, rgba(255,255,255,0.05) 55%, rgba(74,77,85,0.35) 70%, rgba(74,77,85,0) 80%);
  }
  .brand {
    position: absolute;
    left: 67px;
    top: 170px;
    display: flex;
    align-items: center;
    gap: 10px;
    font-weight: 700;
    font-size: 30px;
    line-height: 1;
  }
  .brand-dot {
    width: 16px;
    height: 16px;
    border-radius: 50%;
    background: var(--ink);
  }
  .brand-url {
    position: absolute;
    left: 93px;
    top: 206px;
    font-size: 16px;
    font-weight: 700;
  }
  .code {
    position: absolute;
    left: 62px;
    top: 282px;
    margin: 0;
    font-size: 152px;
    font-weight: 700;
    line-height: 1;
    letter-spacing: -2px;
  }
  .code-name {
    position: absolute;
    left: 67px;
    top: 428px;
    margin: 0;
    font-size: 38px;
    font-weight: 700;
    letter-spacing: 0.5px;
    transform: rotate(-2deg);
    transform-origin: left center;
  }
  .tagline {
    position: absolute;
    left: 67px;
    top: 535px;
    margin: 0;
    font-size: 27px;
    font-weight: 700;
    line-height: 1.08;
    transform: rotate(2deg);
    transform-origin: left center;
  }
  .benefits, .specs {
    position: absolute;
    left: 67px;
    margin: 0;
    padding: 0;
    list-style: none;
    font-size: 13px;
    font-weight: 700;
    line-height: 1.7;
    transform: rotate(3deg);
    transform-origin: left center;
  }
  .benefits { top: 635px; }
  .specs { top: 745px; font-weight: 400; }
  .length {
    position: absolute;
    left: 67px;
    top: 842px;
    font-size: 13px;
    font-weight: 700;
    transform: rotate(3deg);
    transform-origin: left center;
  }
  .origin {
    position: absolute;
    left: 67px;
    top: 878px;
    font-size: 9px;
  }
  .origin svg { display: block; margin-bottom: 3px; }
</style>
</head>
<body>
  <main class="bag">
    <div class="seal-line"></div>
    <div class="product-view" role="img" aria-label="Coiled black optical audio cable with square connectors, seen through the clear bag"></div>

    <div class="brand"><span class="brand-dot"></span><span class="brand-name">Lumen Wire Outlet</span></div>
    <div class="brand-url">lumenwireoutlet.example</div>

    <h1 class="code">OFC</h1>
    <h2 class="code-name">OPTICAL FIBER, CONDUCTIVE</h2>

    <p class="tagline">TONES OF 01100100 01100001<br>01110100 01100001 IN SECONDS</p>

    <ul class="benefits">
      <li>HIGHER BANDWIDTH THAN METAL CABLES</li>
      <li>THIN, LIGHTWEIGHT AND FLEXIBLE</li>
      <li>MORE DURABLE THEN METAL CABLES</li>
    </ul>

    <ul class="specs">
      <li>FIBER COUNTS: 2–4</li>
      <li>TENSILE STRENGTH: 400 N</li>
      <li>DIAMETER: 5 MM</li>
      <li>WEIGHT: 10 G</li>
    </ul>

    <div class="length">1.5 m/ 4.9 ft</div>

    <div class="origin">
      <svg width="68" height="44" viewBox="0 0 68 44" aria-hidden="true">
        <g fill="#ffffff">
          <rect x="0" y="0" width="68" height="3.4"/>
          <rect x="0" y="6.8" width="68" height="3.4"/>
          <rect x="0" y="13.6" width="68" height="3.4"/>
          <rect x="0" y="20.4" width="68" height="3.4"/>
          <rect x="0" y="27.2" width="68" height="3.4"/>
          <rect x="0" y="34" width="68" height="3.4"/>
          <rect x="0" y="40.6" width="68" height="3.4"/>
          <rect x="0" y="0" width="28" height="23.8"/>
        </g>
      </svg>
      Made in the USA
    </div>
  </main>
</body>
</html>
```